Stationary Design Letterhead and Envelope

Artist should provide Letterhead and envelop stationary designs

Info for stationary:
Fernhallow Outdoor Advertising
4873 Quarry Rd. 915 N. PO BOX 528617
Austin, TX 78519

Dale Fernhallow
President
555-862-1907
dale@fernhallowsigns.example
fernhallowsigns.example

Target Market(s)

clients

Colors
0054AA
0677BA
7BADD7
CADEEF
E8F1F8

Requirements
Must have
• high quality unique eye catching and dynamic

```html
<!DOCTYPE html>
<html lang="en">
<head>
<meta charset="utf-8">
<title>Fernhallow Outdoor Advertising — Stationery</title>
<link rel="stylesheet" href="https://fonts.googleapis.com/css2?family=Montserrat:wght@400;500;600;700;800&display=swap">
<style>
  :root {
    --brand-blue: #1c6aa8;
    --brand-blue-light: #2f86c6;
    --ink: #1a1a1a;
    --ink-soft: #555a60;
    --paper: #ffffff;
    --paper-shade: #f6f6f5;
    --backdrop-top: #eeedea;
    --backdrop-mid: #e6e7e8;
    --backdrop-low: #e3e4e5;
  }
  * { box-sizing: border-box; margin: 0; padding: 0; }
  html, body { width: 1200px; height: 2569px; overflow: hidden; }
  body { font-family: "Montserrat", sans-serif; color: var(--ink); position: relative; }

  .scene { position: absolute; left: 0; width: 1200px; }
  .scene--cards { top: 0; height: 948px; background: var(--backdrop-top); }
  .scene--letter { top: 948px; height: 804px; background: var(--backdrop-mid); }
  .scene--envelopes { top: 1752px; height: 817px; background: var(--backdrop-low); }

  .sheet { position: absolute; background: var(--paper); box-shadow: 0 10px 28px rgba(0,0,0,.12); overflow: hidden; }

  /* wordmark */
  .wordmark { display: inline-flex; align-items: center; gap: 8px; font-weight: 800; letter-spacing: .02em; text-transform: uppercase; line-height: 1; color: var(--brand-blue); }
  .wordmark__square { width: .6em; height: .6em; background: currentColor; }
  .wordmark--light { color: var(--paper); }

  /* bottom band */
  .band { position: absolute; left: 0; bottom: 0; width: 100%; display: block; }
  .band .band__blue { fill: var(--brand-blue); }
  .band .band__black { fill: var(--ink); }

  /* business card back */
  .card { width: 560px; height: 320px; }
  .card--back { left: 80px; top: 120px; background: var(--brand-blue); display: flex; align-items: center; justify-content: center; }
  .card--back .wordmark { font-size: 40px; }

  /* business card front */
  .card--front { left: 560px; top: 520px; }
  .card--front .wordmark { position: absolute; right: 36px; top: 48px; font-size: 30px; }
  .card__rule { position: absolute; left: 190px; right: 36px; top: 122px; height: 1px; background: var(--brand-blue-light); }
  .person { position: absolute; left: 40px; top: 176px; }
  .person__name { font-size: 19px; font-weight: 700; letter-spacing: .02em; text-transform: uppercase; }
  .person__role { font-size: 13px; color: var(--brand-blue-light); font-weight: 500; margin-top: 2px; }
  .contacts { list-style: none; font-size: 11.5px; color: var(--ink); }
  .contacts li { display: flex; align-items: center; gap: 7px; margin-top: 4px; }
  .contacts svg { width: 11px; height: 11px; fill: var(--brand-blue); flex: none; }
  .card--front .contacts { position: absolute; left: 40px; top: 222px; }
  .address { font-size: 12px; line-height: 1.45; text-align: right; color: var(--ink); }
  .card--front .address { position: absolute; right: 36px; top: 150px; }

  /* letterhead */
  .letterhead { left: 120px; top: 50px; width: 500px; height: 707px; }
  .letterhead .wordmark { position: absolute; right: 48px; top: 52px; font-size: 24px; }
  .letter { position: absolute; left: 48px; right: 48px; top: 130px; font-size: 9px; line-height: 1.6; color: var(--ink-soft); }
  .letter p { margin-bottom: 10px; }
  .signature { width: 70px; height: 26px; background: #ececec; margin: 6px 0 0; }
  .letterhead .contacts { position: absolute; left: 40px; bottom: 60px; font-size: 9px; }
  .letterhead .contacts svg { width: 9px; height: 9px; }
  .letterhead .address { position: absolute; right: 40px; bottom: 56px; font-size: 9.5px; color: var(--brand-blue); }

  /* envelope back (flap) */
  .envelope { width: 520px; height: 260px; }
  .envelope--back .flap { position: absolute; left: 0; top: 0; width: 100%; height: 48%; background: var(--brand-blue); border-radius: 0 0 14px 14px; display: flex; align-items: center; justify-content: center; }
  .envelope--back .wordmark { font-size: 22px; }
  .scene--letter .envelope--back { left: 640px; top: 270px; }
  .scene--envelopes .envelope--back { left: 600px; top: 120px; }

  /* envelope front */
  .envelope--front { left: 110px; top: 420px; }
  .envelope--front .wordmark { position: absolute; left: 40px; top: 40px; font-size: 22px; }
  .envelope--front .address { position: absolute; left: 40px; top: 84px; text-align: left; font-size: 10.5px; color: var(--brand-blue); }
</style>
</head>
<body>

<svg width="0" height="0" style="position:absolute" aria-hidden="true">
  <symbol id="icon-phone" viewBox="0 0 24 24"><path d="M6.6 10.8a15 15 0 0 0 6.6 6.6l2.2-2.2c.3-.3.7-.4 1-.2 1.1.4 2.3.6 3.6.6.6 0 1 .4 1 1V20c0 .6-.4 1-1 1A17 17 0 0 1 3 4c0-.6.4-1 1-1h3.5c.6 0 1 .4 1 1 0 1.3.2 2.5.6 3.6.1.3 0 .7-.2 1z"/></symbol>
  <symbol id="icon-mail" viewBox="0 0 24 24"><path d="M2 5h20v14H2z M3.5 6.5 12 13l8.5-6.5" /></symbol>
  <symbol id="icon-globe" viewBox="0 0 24 24"><path d="M12 2a10 10 0 1 0 0 20 10 10 0 0 0 0-20zm0 2c1 1.2 1.8 3 2.1 5H9.9C10.2 7 11 5.2 12 4zM4.3 11h3.6c0 .7.1 1.4.2 2H4.3a8 8 0 0 1 0-2zm5.6 0h4.2a14 14 0 0 1 0 2H9.9a14 14 0 0 1 0-2zm6.2 0h3.6a8 8 0 0 1 0 2h-3.6c.1-.6.1-1.3 0-2zM9.9 15h4.2c-.3 2-1.1 3.8-2.1 5-1-1.2-1.8-3-2.1-5z"/></symbol>
</svg>

<!-- Business cards -->
<section class="scene scene--cards">
  <div class="sheet card card--back">
    <span class="wordmark wordmark--light"><span class="wordmark__square"></span>Fernhallow</span>
  </div>

  <div class="sheet card card--front">
    <span class="wordmark"><span class="wordmark__square"></span>Fernhallow</span>
    <div class="card__rule"></div>
    <div class="person">
      <div class="person__name">Dale Fernhallow</div>
      <div class="person__role">President</div>
    </div>
    <ul class="contacts">
      <li><svg><use href="#icon-phone"/></svg>555-862-1907</li>
      <li><svg><use href="#icon-mail"/></svg>dale@fernhallowsigns.example</li>
      <li><svg><use href="#icon-globe"/></svg>www.fernhallowsigns.example</li>
    </ul>
    <div class="address">Fernhallow Outdoor Advertising<br>4873 Quarry Rd. 915 N.<br>PO BOX 528617 Austin, TX 78519</div>
    <svg class="band" viewBox="0 0 560 22" height="22" preserveAspectRatio="none">
      <polygon class="band__blue" points="0,14 372,14 366,22 0,22"/>
      <polygon class="band__black" points="374,4 560,4 560,22 362,22"/>
    </svg>
  </div>
</section>

<!-- Letterhead and envelope -->
<section class="scene scene--letter">
  <div class="sheet letterhead">
    <span class="wordmark"><span class="wordmark__square"></span>Fernhallow</span>
    <div class="letter">
      <p>Dear customer,</p>
      <p>Thank you for choosing us for your next outdoor campaign. Our team plans, prints and installs billboards across the region with care, speed and clear reporting on every placement we deliver for you.</p>
      <p>We will review your goals, suggest strong locations and share a simple schedule. Each board is checked after installation so your message stays bright and easy to read from the road.</p>
      <p>Please reach out with any questions about pricing, artwork sizes or timing. We look forward to working with you.</p>
      <p>Yours Sincerely,</p>
      <div class="signature" role="img" aria-label="Handwritten signature"></div>
    </div>
    <ul class="contacts">
      <li><svg><use href="#icon-phone"/></svg>555-862-1907</li>
      <li><svg><use href="#icon-mail"/></svg>dale@fernhallowsigns.example</li>
      <li><svg><use href="#icon-globe"/></svg>www.fernhallowsigns.example</li>
    </ul>
    <div class="address">Fernhallow Outdoor Advertising<br>4873 Quarry Rd. 915 N.<br>PO BOX 528617 Austin, TX 78519</div>
    <svg class="band" viewBox="0 0 500 20" height="20" preserveAspectRatio="none">
      <polygon class="band__blue" points="0,12 300,12 294,20 0,20"/>
      <polygon class="band__black" points="302,4 500,4 500,20 290,20"/>
    </svg>
  </div>

  <div class="sheet envelope envelope--back">
    <div class="flap"><span class="wordmark wordmark--light"><span class="wordmark__square"></span>Fernhallow</span></div>
  </div>
</section>

<!-- Envelopes -->
<section class="scene scene--envelopes">
  <div class="sheet envelope envelope--back">
    <div class="flap"><span class="wordmark wordmark--light"><span class="wordmark__square"></span>Fernhallow</span></div>
  </div>

  <div class="sheet envelope envelope--front">
    <span class="wordmark"><span class="wordmark__square"></span>Fernhallow</span>
    <div class="address">Fernhallow Outdoor Advertising<br>4873 Quarry Rd. 915 N.<br>PO BOX 528617 Austin, TX 78519</div>
    <svg class="band" viewBox="0 0 520 20" height="20" preserveAspectRatio="none">
      <polygon class="band__blue" points="0,12 312,12 306,20 0,20"/>
      <polygon class="band__black" points="314,4 520,4 520,20 302,20"/>
    </svg>
  </div>
</section>

</body>
</html>
```